Redesign of business card for Birchline Mechanical

We are looking for a new design for our business cards for Birchline Mechanical. We are a plumbing & HVAC construction company, operating on the West Coast of Canada and USA. Logo attached.
Industry/Entity Type
Construction - Plumbing & HVAC
Contact Information for Business Card
Name, address, phone numbers, email, website address
Look and feel
Each slider illustrates characteristics of the customer's brand and the style your logo design should communicate.

```html
<!DOCTYPE html>
<html lang="en">
<head>
<meta charset="utf-8">
<title>Birchline Mechanical – Business Card</title>
<link href="https://fonts.googleapis.com/css2?family=Poppins:wght@400;500;700&display=swap" rel="stylesheet">
<style>
  :root {
    --backdrop: #c8c8c8;
    --card-light: #ffffff;
    --card-dark: #2a2a2a;
    --ink: #111111;
    --ink-soft: #2b2b2b;
    --on-dark: #ffffff;
    --accent-dark: #3d3d3d;
  }
  * { margin: 0; padding: 0; box-sizing: border-box; }
  html, body { width: 800px; height: 1200px; overflow: hidden; }
  body {
    background: var(--backdrop);
    font-family: "Poppins", Arial, sans-serif;
    position: relative;
  }
  .card {
    position: absolute;
    left: 182px;
    width: 436px;
    height: 262px;
    overflow: hidden;
    box-shadow: 2px 3px 5px rgba(0,0,0,0.25);
  }
  .card--front { top: 311px; background: var(--card-light); }
  .card--back  { top: 629px; background: var(--card-dark); color: var(--on-dark); }

  .wordmark {
    position: absolute;
    display: flex;
    align-items: center;
    gap: 8px;
    font-weight: 500;
    letter-spacing: 0.5px;
    white-space: nowrap;
  }
  .wordmark__square { width: 14px; height: 14px; flex: none; }
  .card--front .wordmark {
    left: 50%; top: 120px; transform: translateX(-50%);
    font-size: 20px; color: var(--ink);
  }
  .card--front .wordmark__square { background: var(--ink); }
  .card--back .wordmark {
    left: 40px; top: 82px;
    font-size: 14px; color: var(--on-dark);
  }
  .card--back .wordmark__square { width: 11px; height: 11px; background: var(--on-dark); }

  .website {
    position: absolute; left: 0; right: 0; top: 218px;
    text-align: center; font-size: 9.5px; letter-spacing: 2.6px; color: var(--ink-soft);
  }

  .holder { position: absolute; left: 56px; top: 168px; }
  .holder__name { font-size: 15px; line-height: 1.2; font-weight: 400; }
  .holder__name strong { font-weight: 700; }
  .holder__role { font-size: 9.5px; margin-top: 2px; }

  .circle { position: absolute; border-radius: 50%; background: var(--accent-dark); }
  .circle--small { left: 363px; top: 164px; width: 22px; height: 22px; }
  .circle--large { left: 368px; top: 187px; width: 68px; height: 68px; }

  .contacts { position: absolute; left: 248px; top: 163px; list-style: none; font-size: 9.8px; line-height: 13px; }
  .contacts li { display: flex; align-items: flex-start; gap: 8px; margin-bottom: 4px; position: relative; }
  .contacts svg { width: 9px; height: 9px; flex: none; margin-top: 2px; fill: var(--on-dark); }
</style>
</head>
<body>
  <section class="card card--front" aria-label="Business card front">
    <div class="wordmark"><span class="wordmark__square"></span>Birchline Mechanical</div>
    <p class="website">www.birchlinemech.com</p>
  </section>

  <section class="card card--back" aria-label="Business card back">
    <div class="wordmark"><span class="wordmark__square"></span>Birchline Mechanical</div>

    <div class="holder">
      <p class="holder__name"><strong>Lorem</strong> Ipsum</p>
      <p class="holder__role">CEO &amp; Founder</p>
    </div>

    <span class="circle circle--small"></span>
    <span class="circle circle--large"></span>

    <ul class="contacts">
      <li>
        <svg viewBox="0 0 24 24" aria-hidden="true"><path d="M6.6 10.8a15 15 0 0 0 6.6 6.6l2.2-2.2c.3-.3.7-.4 1-.2 1.1.4 2.3.6 3.6.6.6 0 1 .4 1 1V20c0 .6-.4 1-1 1A17 17 0 0 1 3 4c0-.6.4-1 1-1h3.5c.6 0 1 .4 1 1 0 1.3.2 2.5.6 3.6.1.3 0 .7-.2 1z"/></svg>
        <span>555-014-2290</span>
      </li>
      <li>
        <svg viewBox="0 0 24 24" aria-hidden="true"><path d="M2 5h20v14H2z M2 5l10 8 10-8" fill="none" stroke="#fff" stroke-width="2.5"/></svg>
        <span>info@birchlinemech.com</span>
      </li>
      <li>
        <svg viewBox="0 0 24 24" aria-hidden="true"><path d="M12 2a7 7 0 0 0-7 7c0 5 7 13 7 13s7-8 7-13a7 7 0 0 0-7-7zm0 9.5A2.5 2.5 0 1 1 12 6.5a2.5 2.5 0 0 1 0 5z"/></svg>
        <span>418 Harbor Crest Way,<br>Suite 200, Tustin, CA 92780</span>
      </li>
    </ul>
  </section>
</body>
</html>
```